Letterhead Design Project

We have just had a letterhead desinged on word which is pretty basic and boring. We are looking for a professional and modern letterhead to suit our business for letters and quotes. We are an irrigation business that looks at providing a garden enhancement package. We do instore sales, internet sales and design and installation. We would like the colours to be similar to what is on our website. www.dunsfordwatering.com.au
Industry/Entity Type
Internet
Requirements
Must have
- We would like to include:
find us on facebook and twitter,
member of sprinquest stores,
Catchphrase: "The Garden Enhancement Specialist"
Approved Watering Stockist Logo
phone, fax, email & website

```html
<!DOCTYPE html>
<html lang="en">
<head>
<meta charset="utf-8">
<title>Dunsford Watering Supplies – Letterhead</title>
<link rel="stylesheet" href="https://fonts.googleapis.com/css2?family=PT+Sans:wght@400;700&display=swap">
<style>
  :root {
    --brand-blue: #1a7fcf;
    --brand-blue-dark: #0f63a8;
    --logo-panel-top: #d9ecfa;
    --logo-panel-bottom: #9cc9ec;
    --corner-grey: #e4e6e9;
    --page: #ffffff;
    --ink: #3a3a3a;
    --ink-soft: #555a60;
    --rule: #9cb8d6;
    --web-blue: #1a8fd6;
    --badge-ring: #2b8fd4;
    --badge-fill: #e9f3fb;
  }
  * { box-sizing: border-box; margin: 0; padding: 0; }
  html, body { width: 1058px; height: 1200px; overflow: hidden; background: var(--page); }
  body { font-family: "PT Sans", "Myriad Pro", Arial, sans-serif; color: var(--ink); }

  .letterhead { position: relative; width: 1058px; height: 1200px; background: var(--page); }

  .header-art { position: absolute; left: 0; top: 0; width: 1058px; height: 230px; }

  .brand-panel {
    position: absolute; left: 60px; top: 92px; width: 270px; height: 78px;
    border: 2px solid #eaf4fc; border-radius: 4px;
    background: linear-gradient(to bottom, var(--logo-panel-top), var(--logo-panel-bottom));
    display: flex; align-items: center; gap: 10px; padding: 0 16px;
  }
  .brand-dot { width: 18px; height: 18px; border-radius: 50%; background: var(--brand-blue); flex: none; }
  .brand-name { font-size: 24px; font-weight: 400; color: #1d3d5c; white-space: nowrap; }

  .tagline {
    position: absolute; left: 352px; top: 150px;
    font-size: 20px; color: #ffffff; letter-spacing: 0.3px;
  }

  .recipient { position: absolute; left: 150px; top: 300px; font-size: 17px; line-height: 21px; color: var(--ink-soft); }
  .recipient .recipient-name { font-weight: 700; color: #222; }

  .letter-body {
    position: absolute; left: 170px; top: 470px; width: 650px;
    font-size: 15.5px; line-height: 21px; color: var(--ink-soft); text-align: justify;
  }
  .letter-body p { margin-bottom: 21px; }

  .signature { position: absolute; left: 170px; top: 880px; font-size: 16px; line-height: 21px; color: var(--ink-soft); }
  .signature .signer { color: #111; font-size: 17px; }

  .footer-rule { position: absolute; left: 150px; top: 1080px; width: 790px; height: 1px; background: var(--rule); }

  .contact { position: absolute; left: 150px; top: 1092px; font-size: 14px; line-height: 19px; color: var(--ink-soft); }
  .contact .web-emph { color: var(--web-blue); }
  .contact-line { display: flex; align-items: center; gap: 14px; }
  .contact-item { display: inline-flex; align-items: center; gap: 5px; }

  .social { position: absolute; left: 525px; top: 1040px; display: flex; align-items: center; gap: 6px; font-size: 15px; color: var(--ink-soft); }
  .social-square { width: 22px; height: 22px; border-radius: 3px; background: var(--web-blue); }
  .social-square.alt { background: #3b5a98; }

  .membership { position: absolute; left: 690px; top: 1044px; font-size: 13px; color: #7a7f85; }

  .stockist-badge { position: absolute; left: 860px; top: 960px; width: 110px; height: 110px; }
</style>
</head>
<body>
<main class="letterhead">
  <svg class="header-art" viewBox="0 0 1058 230" aria-hidden="true">
    <polygon points="860,0 1058,0 1058,160" fill="var(--corner-grey)"/>
    <polygon points="0,60 860,30 1058,160 1058,220 0,220" fill="var(--brand-blue)"/>
    <polygon points="0,205 1058,205 1058,220 0,220" fill="var(--brand-blue-dark)" opacity="0.35"/>
  </svg>

  <div class="brand-panel">
    <span class="brand-dot"></span>
    <span class="brand-name">Dunsford Watering</span>
  </div>
  <div class="tagline">The Garden Enhancement Specialist</div>

  <address class="recipient" style="font-style:normal">
    <div class="recipient-name">Mr. Owen Hartley</div>
    <div>Managing Director</div>
    <div>Northgate Holdings</div>
    <div>48 Harbour Lane</div>
    <div>USA</div>
  </address>

  <section class="letter-body">
    <p>Lorem Ipsum is simply dummy text for printing and typesetting industry. Lorem Ipsum has been the industry's standard dummy text since the 1500s, when an unknown printer galley of type and scrambled it to make a type specimen book. It has suvived not only manual but also the leap into electronic typesetting, remaining essentially unchanged. It was popularised in the 1960s with the release of Typeset sheets containing Lorem Ipsum pass and more recently with desktop publishing software like Folio PageWriter including version 6.9 of Lorem Ipsum.</p>
    <p>Country to popular belief, Lorem Ipsum is not simply random text. It has roots in a piece of sical Latin literature from 45 BC, making it over 2000 years old. Rupert Mallory, a prfessor at Ashcombe College in Vermont, looked up one of the most obscure world classical literature, discovered the undoubtable sorce. Lorem Ipsum comes from section 1.10.32 and 1.10.33 of "de Finibus Bonorum et Molorum" (The Extreme of Good and Even Cicero), written in 45 BC. This book is a treatise on the theory of ethics very popular during Renassiance.</p>
    <p>Thank you for being one of our valued customers.</p>
  </section>

  <div class="signature">
    <div class="signer">Name Here</div>
    <div>CEO</div>
    <div>Dunsford Watering</div>
  </div>

  <div class="social">
    <span>find us on</span>
    <span class="social-square"></span>
    <span class="social-square alt"></span>
  </div>
  <div class="membership">Member of Sprinquest Store</div>

  <svg class="stockist-badge" viewBox="0 0 110 110" role="img" aria-label="Approved Watering Stockist badge">
    <circle cx="55" cy="55" r="52" fill="var(--badge-ring)"/>
    <circle cx="55" cy="55" r="40" fill="var(--badge-fill)"/>
  </svg>

  <div class="footer-rule"></div>

  <div class="contact">
    <div>212 Fernleigh Rd Dunsford.</div>
    <div class="contact-line">
      <span class="contact-item">
        <svg width="12" height="12" viewBox="0 0 12 12" aria-hidden="true"><circle cx="6" cy="6" r="6" fill="var(--web-blue)"/><path d="M4 3.2 L5 3 L5.6 4.6 L5 5.2 Q5.8 6.6 6.8 7 L7.4 6.4 L9 7 L8.8 8 Q6.8 9 4.6 6.6 Q3 4.6 4 3.2Z" fill="#fff"/></svg>
        03 9400 1188
      </span>
      <span class="contact-item">
        <svg width="12" height="12" viewBox="0 0 12 12" aria-hidden="true"><circle cx="6" cy="6" r="5.3" fill="none" stroke="var(--web-blue)" stroke-width="1.2"/><ellipse cx="6" cy="6" rx="2.3" ry="5.3" fill="none" stroke="var(--web-blue)" stroke-width="1"/><line x1="0.7" y1="6" x2="11.3" y2="6" stroke="var(--web-blue)" stroke-width="1"/></svg>
        www.<span class="web-emph">dunsfordwatering</span>.com.au
      </span>
    </div>
  </div>
</main>
</body>
</html>
```